依頼詳細
角2、長3、長3窓付きの封筒デザインをお願い致します。
(長3は長3窓付きは共通のデザインで良いです。)
封筒は白を予定しています。
記載項目
サニーリンクホーダ
〒951-0417 新潟県長岡市西柳台5-8-2
TEL 090-7185-2946 FAX 0258-31-9087
希望イメージ
シンプル 複雑
単色 カラフル
暗い 明るい
日常 高級
遊び心 厳粛
未来的 伝統的
女性的 男性的
希望する色
青系、緑系
納品ファイル
補足説明
ロゴの添付ファイルあり
印刷通販のプリモアで封筒印刷(刷込)を予定。

■ 選んだ理由

ロゴと社名、アドレス、そして封筒のデザインに対して
封筒の余白のバランスが自分のイメージに合っていたと思います。

■ 提案者全員のお礼・コメント

さすがプロのデザイナーだけあってそれぞれ素晴らしい提案で
選考するのが大変でした。
提案して頂いたパドラーの皆様ありがとうございました。

```html
<!DOCTYPE html>
<html lang="ja">
<head>
<meta charset="utf-8">
<title>サニーリンクホーダ 角2封筒</title>
<link rel="stylesheet" href="https://fonts.googleapis.com/css2?family=Noto+Sans+JP:wght@400;500;700&display=swap">
<style>
  :root {
    --backdrop: #f4f5f6;
    --paper: #ffffff;
    --edge: #c9ccd0;
    --ink: #3a3f45;
    --brand-blue: #2f7fc4;
    --band-deep: rgba(47, 127, 196, 0.55);
    --band-light: rgba(140, 198, 236, 0.35);
    --band-clear: rgba(140, 198, 236, 0);
  }
  html, body {
    margin: 0;
    padding: 0;
    width: 849px;
    height: 1200px;
    overflow: hidden;
    background: var(--backdrop);
    font-family: "Noto Sans JP", sans-serif;
    color: var(--ink);
  }
  .envelope {
    position: absolute;
    left: 112px;
    top: 58px;
    width: 630px;
    height: 1074px;
    background: var(--paper);
    border: 1px solid var(--edge);
    box-shadow: 0 2px 6px rgba(0,0,0,0.12);
    box-sizing: border-box;
  }
  .envelope__flap {
    position: absolute;
    left: 0;
    top: 0;
    width: 100%;
    height: 70px;
  }
  .brand {
    position: absolute;
    left: 34px;
    top: 878px;
    width: 150px;
    display: flex;
    flex-direction: column;
    align-items: center;
    gap: 10px;
  }
  .brand__dot {
    width: 66px;
    height: 66px;
    border-radius: 50%;
    background: var(--brand-blue);
  }
  .brand__name {
    font-size: 15px;
    font-weight: 500;
    color: var(--brand-blue);
    letter-spacing: 0.03em;
    white-space: nowrap;
  }
  .sender {
    position: absolute;
    left: 194px;
    top: 884px;
    line-height: 1.5;
  }
  .sender__company {
    font-size: 14px;
    font-weight: 700;
    letter-spacing: 0.06em;
    margin: 0 0 3px;
  }
  .sender__line {
    font-size: 9px;
    margin: 0;
    letter-spacing: 0.03em;
  }
  .wave-band {
    position: absolute;
    left: 170px;
    top: 945px;
    width: 459px;
    height: 56px;
    background:
      linear-gradient(to right, var(--band-clear) 0%, var(--band-light) 35%, var(--band-deep) 70%, var(--band-light) 100%);
    -webkit-mask-image: linear-gradient(to bottom, transparent 0%, #000 40%, #000 60%, transparent 100%);
    mask-image: linear-gradient(to bottom, transparent 0%, #000 40%, #000 60%, transparent 100%);
  }
</style>
</head>
<body>
  <div class="envelope">
    <svg class="envelope__flap" viewBox="0 0 630 70" preserveAspectRatio="none">
      <path d="M0 10 L20 62 Q315 72 610 62 L630 10" fill="none" stroke="var(--edge)" stroke-width="1.2"/>
    </svg>

    <div class="brand">
      <div class="brand__dot"></div>
      <div class="brand__name">Sunny Link Hoda</div>
    </div>

    <div class="sender">
      <p class="sender__company">サニーリンクホーダ</p>
      <p class="sender__line">〒951-0417 新潟県長岡市西柳台5-8-2</p>
      <p class="sender__line">TEL 090-7185-2946 FAX 0258-31-9087</p>
    </div>

    <div class="wave-band" role="img" aria-label="青いグラデーションの波模様の装飾が入る領域"></div>
  </div>
</body>
</html>
```